Life Coach for Lawyers Business Card Design

Elegant, original, business card design for life coaching service for associate attorneys who work in big law and struggle with stress, overwhelm, and time management. Double sided design.

Target Market(s)

Women associate attorneys who work in big law and struggle with stress, overwhelm, and time management.

Industry/Entity Type

Life Coaching

Contact Information for Business Card

Marissa Pendrell
Life Coach
518.677.3941
calmbriefcounsel.net
marissa@calmbriefcounsel.net
@calmbriefcounsel (Instagram)

Font styles to use
Other font styles liked:
• Silver South font duo. See uploaded files.

Requirements
Must have
• Icons for phone, website, email, and Instagram instead of words. Specific colors used in my logo (171B2B, 421121, FFFFFF)
Nice to have
• Foil. Embossed. Feminine design.
Should not have
• Any colors other than those used in logo. See uploaded files.

```html
<!DOCTYPE html>
<html lang="en">
<head>
<meta charset="utf-8">
<title>Calm Brief Counsel — Business Card</title>
<link rel="stylesheet" href="https://fonts.googleapis.com/css2?family=Playfair+Display:wght@400&family=Roboto:wght@400&display=swap">
<style>
  :root {
    --navy: #171B2B;
    --wine: #421121;
    --white: #FFFFFF;
    --page: #FFFFFF;
  }
  * { margin: 0; padding: 0; box-sizing: border-box; }
  html, body {
    width: 1200px; height: 1200px; overflow: hidden;
    background: var(--page);
  }
  .canvas { position: relative; width: 1200px; height: 1200px; }
  .card {
    position: absolute; width: 746px; height: 459px; overflow: hidden;
  }
  .card--front { left: 267px; top: 124px; background: var(--navy); }
  .card--back  { left: 269px; top: 636px; background: var(--white); }
  .card__waves { position: absolute; inset: 0; width: 746px; height: 459px; }

  .brand {
    position: absolute; left: 0; right: 0; text-align: center;
    font-family: "Playfair Display", Georgia, serif; font-weight: 400;
    letter-spacing: 2px; white-space: nowrap; line-height: 1;
  }
  .card--front .brand { top: 86px; font-size: 64px; color: var(--white); }
  .card--back  .brand { top: 88px; font-size: 52px; color: var(--navy); }

  .site-line {
    position: absolute; left: 0; right: 0; top: 402px;
    display: flex; align-items: center; justify-content: center; gap: 10px;
    font-family: "Roboto", Arial, sans-serif; font-size: 22px; color: var(--white);
  }
  .site-line__rule { width: 74px; height: 8px; }

  .holder {
    position: absolute; right: 20px; top: 232px; text-align: right;
    font-family: "Roboto", Arial, sans-serif; color: var(--white);
  }
  .holder__name { font-size: 32px; line-height: 38px; }
  .holder__role { font-size: 22px; line-height: 26px; }

  .contacts {
    position: absolute; left: 41px; top: 300px; list-style: none;
    font-family: "Roboto", Arial, sans-serif; font-size: 20px; color: var(--white);
  }
  .contacts__item { display: flex; align-items: center; height: 28px; margin-bottom: 7px; }
  .contacts__item:last-child { margin-bottom: 0; }
  .contacts__icon { width: 28px; height: 28px; margin-right: 16px; flex: none; }
</style>
</head>
<body>
<main class="canvas">

  <section class="card card--front" aria-label="Card front">
    <svg class="card__waves" viewBox="0 0 746 459" aria-hidden="true">
      <path fill="var(--wine)" d="M0 280 C250 240 480 215 630 220 C700 224 740 240 746 262 L746 459 L0 459 Z"/>
      <path fill="var(--navy)" d="M0 334 C260 290 520 265 640 272 C700 276 735 292 746 318 L746 330 C735 306 700 290 640 287 C520 282 260 306 0 344 Z"/>
    </svg>
    <div class="brand">Calm Brief Counsel</div>
    <div class="site-line">
      <svg class="site-line__rule" viewBox="0 0 74 8" aria-hidden="true"><path fill="var(--white)" d="M0 4 L74 1 L74 7 Z"/></svg>
      <span>www.calmbriefcounsel.net</span>
      <svg class="site-line__rule" viewBox="0 0 74 8" aria-hidden="true"><path fill="var(--white)" d="M0 1 L74 4 L0 7 Z"/></svg>
    </div>
  </section>

  <section class="card card--back" aria-label="Card back">
    <svg class="card__waves" viewBox="0 0 746 459" aria-hidden="true">
      <path fill="var(--navy)" d="M0 0 L746 0 C715 25 660 42 580 42 C420 42 200 20 0 0 Z"/>
      <path fill="var(--wine)" d="M0 0 L746 0 C712 22 655 37 575 37 C420 37 200 18 0 0 Z"/>
      <path fill="var(--navy)" d="M0 256 C240 210 500 180 640 182 C700 183 735 192 746 202 L746 459 L0 459 Z"/>
      <path fill="var(--wine)" d="M0 270 C240 224 500 195 640 196 C700 197 735 205 746 214 L746 459 L0 459 Z"/>
    </svg>
    <div class="brand">Calm Brief Counsel</div>

    <div class="holder">
      <div class="holder__name">Marissa Pendrell</div>
      <div class="holder__role">Life Coach</div>
    </div>

    <ul class="contacts">
      <li class="contacts__item">
        <svg class="contacts__icon" viewBox="0 0 32 32" aria-label="Phone">
          <circle cx="16" cy="16" r="16" fill="var(--white)"/>
          <path fill="var(--navy)" d="M11 8.5c.8-.5 1.7-.3 2.1.5l1.3 2.6c.3.7.1 1.4-.5 1.8l-1 .7c.6 1.9 2 3.6 3.7 4.7l.9-.9c.5-.5 1.3-.6 1.9-.2l2.4 1.6c.7.5.9 1.4.4 2.1l-.9 1.3c-.6.8-1.6 1.1-2.6.8-4.6-1.5-8.1-5.5-9.2-10.2-.2-1 .2-2 1-2.6z"/>
          <path fill="none" stroke="var(--navy)" stroke-width="1.2" stroke-linecap="round" d="M18 9.5a5 5 0 0 1 4.5 4.5M18 12a2.6 2.6 0 0 1 2 2"/>
        </svg>
        <span>518.677.3941</span>
      </li>
      <li class="contacts__item">
        <svg class="contacts__icon" viewBox="0 0 32 32" aria-label="Email">
          <circle cx="16" cy="16" r="16" fill="var(--white)"/>
          <rect x="8.5" y="11" width="15" height="10" fill="none" stroke="var(--navy)" stroke-width="1.6"/>
          <path fill="none" stroke="var(--navy)" stroke-width="1.4" d="M8.5 11l7.5 6 7.5-6M8.5 21l5.5-5M23.5 21l-5.5-5"/>
        </svg>
        <span>marissa@calmbriefcounsel.net</span>
      </li>
      <li class="contacts__item">
        <svg class="contacts__icon" viewBox="0 0 32 32" aria-label="Website">
          <circle cx="16" cy="16" r="16" fill="var(--white)"/>
          <circle cx="16" cy="16" r="9" fill="var(--navy)"/>
          <path fill="var(--white)" d="M12 10.5c2 .5 3 2 2 3.5s-3 1-3.5 3 1 3 .5 4.5c-1.5-1-3-3-3-5.5 0-2.3 1.5-4.5 4-5.5zM19 15c1.5 0 3 1 3.5 2.5-.5 2-2 3.6-3.8 4.3-.5-1.5.5-2.5-.5-3.8-.8-1.2.3-3 .8-3z"/>
        </svg>
        <span>www.calmbriefcounsel.net</span>
      </li>
      <li class="contacts__item">
        <svg class="contacts__icon" viewBox="0 0 32 32" aria-label="Social handle">
          <circle cx="16" cy="16" r="16" fill="var(--white)"/>
        </svg>
        <span>@calmbriefcounsel</span>
      </li>
    </ul>
  </section>

</main>
</body>
</html>
```